Customs House descriptive business cards

We require a two-sided business card that has a simple yet elegant design. We want to be able to promote our services as a customs house. This card should include our logo, contact info and services offered with the logo being on one side and the contact info and services on the flip side

Target Market(s)

Importers / exporters to and from the Bahamas

Industry/Entity Type

Logistics

Contact Information for Business Card

The front side of the card could have the logo and the flip side should have the other relevant info

Font styles to use
Serif

Colors

Designer to choose colors to be used in the design.

Requirements
Must have
• (Harbourline Agents Ltd) Logo, address and contact info also services:
• import customs clearance, Delivery & HAndling services,Florida pickups, Export packing & Crating Services, export customs clearance, Consulting

```html
<!DOCTYPE html>
<html lang="en">
<head>
<meta charset="utf-8">
<title>Harbourline Agents Ltd — Business Card</title>
<link href="https://fonts.googleapis.com/css2?family=Playfair+Display:wght@700&family=Montserrat:wght@400;600&display=swap" rel="stylesheet">
<style>
  :root {
    --backdrop: #e9e7e4;
    --card-black: #141414;
    --card-charcoal: #1c1c1d;
    --logo-grey: #6f6f72;
    --emboss-dark: #262628;
    --emboss-light: #303033;
    --brand-blue: #1f82d6;
    --text-light: #f1f1f1;
    --text-muted: #bdbdc0;
    --icon-blue: #4a9be0;
  }
  * { box-sizing: border-box; margin: 0; padding: 0; }
  html, body {
    width: 1200px;
    height: 875px;
    overflow: hidden;
    background: var(--backdrop);
  }
  .canvas {
    width: 1200px;
    height: 875px;
    display: flex;
    align-items: center;
    justify-content: center;
    gap: 60px;
  }
  .card {
    width: 525px;
    height: 300px;
    border-radius: 4px;
    position: relative;
    overflow: hidden;
    box-shadow: 0 10px 28px rgba(0,0,0,0.22);
  }

  /* Front */
  .card--front {
    background: var(--card-black);
    display: flex;
    align-items: center;
    justify-content: center;
    gap: 18px;
  }
  .brand-mark {
    width: 54px;
    height: 54px;
    background: var(--emboss-light);
    border-radius: 3px;
    flex: none;
  }
  .wordmark {
    font-family: "Playfair Display", Georgia, serif;
    font-weight: 700;
    text-transform: uppercase;
    line-height: 1.1;
  }
  .wordmark--front {
    color: var(--logo-grey);
    font-size: 30px;
    letter-spacing: 2px;
  }

  /* Back */
  .card--back {
    background: var(--card-charcoal);
    padding: 26px 32px;
  }
  .wordmark--back {
    color: var(--brand-blue);
    font-size: 24px;
    letter-spacing: 1.5px;
    margin-bottom: 16px;
  }
  .back-columns {
    display: flex;
    gap: 22px;
    position: relative;
    z-index: 1;
  }
  .contact-column { width: 252px; flex: none; }
  .holder-name {
    font-family: "Playfair Display", Georgia, serif;
    font-weight: 700;
    color: var(--brand-blue);
    font-size: 21px;
    line-height: 1.2;
  }
  .holder-role {
    font-family: "Montserrat", Arial, sans-serif;
    color: var(--text-light);
    font-size: 12px;
    margin: 3px 0 12px;
  }
  .contact-list {
    list-style: none;
    font-family: "Montserrat", Arial, sans-serif;
    color: var(--text-light);
    font-size: 12px;
  }
  .contact-list li {
    display: flex;
    align-items: center;
    gap: 8px;
    margin-bottom: 6px;
    white-space: nowrap;
  }
  .contact-icon { width: 12px; height: 12px; flex: none; }
  .contact-address {
    font-family: "Montserrat", Arial, sans-serif;
    color: var(--text-light);
    font-size: 12.5px;
    margin-top: 9px;
    white-space: nowrap;
  }
  .services-column { flex: 1; }
  .services-title {
    font-family: "Montserrat", Arial, sans-serif;
    font-weight: 600;
    color: var(--brand-blue);
    font-size: 11px;
    letter-spacing: 1.5px;
    text-transform: uppercase;
    margin-bottom: 8px;
  }
  .services-list {
    list-style: none;
    font-family: "Montserrat", Arial, sans-serif;
    color: var(--text-muted);
    font-size: 11px;
    line-height: 1.55;
  }
  .services-list li::before {
    content: "";
    display: inline-block;
    width: 4px;
    height: 4px;
    background: var(--brand-blue);
    margin: 0 7px 2px 0;
    vertical-align: middle;
  }
  .emboss-accent {
    position: absolute;
    right: 0;
    bottom: 0;
    width: 84px;
    height: 84px;
    background: linear-gradient(135deg, var(--emboss-light), var(--emboss-dark));
  }
</style>
</head>
<body>
  <main class="canvas">
    <section class="card card--front" aria-label="Card front">
      <span class="brand-mark" aria-hidden="true"></span>
      <p class="wordmark wordmark--front">Harbourline<br>Agents Ltd.</p>
    </section>

    <section class="card card--back" aria-label="Card back">
      <p class="wordmark wordmark--back">Harbourline Agents Ltd.</p>
      <div class="back-columns">
        <div class="contact-column">
          <p class="holder-name">Daniel Rourke</p>
          <p class="holder-role">Managing Director</p>
          <ul class="contact-list">
            <li>
              <svg class="contact-icon" viewBox="0 0 24 24" aria-hidden="true"><path fill="var(--icon-blue)" d="M6.6 10.8a15 15 0 0 0 6.6 6.6l2.2-2.2c.3-.3.7-.4 1-.2 1.1.4 2.3.6 3.6.6.6 0 1 .4 1 1V20c0 .6-.4 1-1 1A17 17 0 0 1 3 4c0-.6.4-1 1-1h3.5c.6 0 1 .4 1 1 0 1.3.2 2.5.6 3.6.1.3 0 .7-.2 1z"/></svg>
              000.000.0000
            </li>
            <li>
              <svg class="contact-icon" viewBox="0 0 24 24" aria-hidden="true"><rect x="2" y="5" width="20" height="14" rx="2" fill="none" stroke="var(--icon-blue)" stroke-width="2"/><path d="M2 6l10 7 10-7" fill="none" stroke="var(--icon-blue)" stroke-width="2"/></svg>
              drourke@harbourlineagents.com
            </li>
            <li>
              <svg class="contact-icon" viewBox="0 0 24 24" aria-hidden="true"><g fill="none" stroke="var(--icon-blue)" stroke-width="2"><circle cx="12" cy="12" r="10"/><path d="M2 12h20M12 2c3 3 3 17 0 20M12 2c-3 3-3 17 0 20"/></g></svg>
              www.harbourlineagents.com
            </li>
          </ul>
          <p class="contact-address">PO Box 412 Nassau, New Providence</p>
        </div>
        <div class="services-column">
          <p class="services-title">Our Services</p>
          <ul class="services-list">
            <li>Import Customs Clearance</li>
            <li>Delivery &amp; Handling</li>
            <li>Florida Pickups</li>
            <li>Export Packing &amp; Crating</li>
            <li>Export Customs Clearance</li>
            <li>Consulting</li>
          </ul>
        </div>
      </div>
      <div class="emboss-accent" role="img" aria-label="Faint embossed brand accent area"></div>
    </section>
  </main>
</body>
</html>
```